Design the web for "http://www.talvoxa-demo.com"

Talvoxa is an open source customer communication platform, think as ZESTORA.IO alternative.

Talvoxa web site is an entry to let people know Talvoxa and try Talvoxa online Talvoxa service.

1, To design the web site, suggest try Talvoxa first.

2, At least replace the original pictures which Talvoxa web site now use. (All got from fennel vault site, shame and not reasonable)

3, Provide total web design, Picture and Code.

Thanks,
Talvoxa owner
Weimin Tao
taoweimin@mailvanta-demo.com

Reason: So far no useful design, and only five designers submit their designs. And one man submit 48 designs, most of his design is same style. I request to extend the deadline, and invite more designers. Thanks, Weimin

Target Market(s)

Open Source.

Industry/Entity Type

Software

Coding

Coded - Design and coding required

Number of Pages Required

2 page

Font styles to use
Sans Serif

Requirements
Must have
• 1) Try Talvoxa first
• 2) Replace all the pictures in the current site.
• 3) Match with the Talvxa features (Customer Communication / Open Source / Open API etc.)
• 4) Download page presents Talvoxa support all kinds of platforms since Talvoxa has all kinds of application for different OS.
• 5) Web style tuning (The current style copy from fennel vault)
• 6) All pictures and web code.
Nice to have
• 1) Logo tuning for the new web style and logo file attached.
• 2) Extremely simple style is prefer.
Should not have
• No

```html
<!DOCTYPE html>
<html lang="en">
<head>
<meta charset="utf-8">
<title>Talvoxa — Customer Communication Platform</title>
<link href="https://fonts.googleapis.com/css2?family=Montserrat:wght@400;600;700&family=Open+Sans:wght@400;600&display=swap" rel="stylesheet">
<style>
:root{
  --teal:#3fbfd2;
  --teal-dark:#2aa6b8;
  --ink:#2e2e2e;
  --text:#666a70;
  --muted:#9aa0a6;
  --rule:#e4e6e8;
  --dark:#2b2b2b;
  --darker:#1f1f1f;
  --white:#ffffff;
}
*{box-sizing:border-box;margin:0;padding:0}
html,body{width:1200px;height:3296px;overflow:hidden}
body{font-family:"Open Sans",Arial,sans-serif;color:var(--text);background:var(--white);font-size:14px;line-height:1.7}
h1,h2,h3,h4,.nav,.btn,.brand{font-family:"Montserrat",Arial,sans-serif}
.btn{display:inline-block;background:var(--teal);color:var(--white);font-size:12px;font-weight:600;letter-spacing:1px;text-transform:uppercase;padding:12px 30px;border:0;white-space:nowrap}

/* hero */
.hero{position:relative;height:600px;background:linear-gradient(180deg,#3c4248 0%,#5b6168 45%,#4a4f55 75%,#2f3338 100%);color:var(--white);text-align:center}
.hero-bg{position:absolute;inset:0;background:linear-gradient(90deg,rgba(30,32,36,.55),rgba(120,126,132,.15) 50%,rgba(30,32,36,.5))}
.topbar{position:relative;height:88px;display:flex;align-items:center;justify-content:space-between;padding:0 80px;background:rgba(20,22,25,.35)}
.brand{display:flex;align-items:center;gap:10px;font-size:26px;font-weight:600;color:var(--white)}
.brand-square{width:34px;height:34px;background:var(--white)}
.nav{display:flex;gap:44px;align-items:center;font-size:12px;font-weight:600;letter-spacing:1px}
.hero-copy{position:relative;padding-top:118px}
.hero h1{font-size:60px;font-weight:700;line-height:1.15;letter-spacing:1px}
.hero p{font-size:17px;margin:28px 0 40px;opacity:.9}

/* about */
.about{height:448px;padding:80px 90px 0;display:flex;justify-content:space-between}
.about-text{width:540px}
h2.section-title{font-size:30px;font-weight:700;color:var(--ink);letter-spacing:1px}
.kicker{font-family:"Montserrat",Arial,sans-serif;font-size:13px;color:var(--ink);font-weight:600;margin-top:10px}
.accent-rule{width:56px;height:3px;background:var(--teal);margin:22px 0 26px}
.about-text p{font-size:13px;margin-bottom:14px}
.video{width:410px;height:272px;margin-top:10px;background:linear-gradient(135deg,#1c2a33,#2d4a58 55%,#16222a);position:relative;box-shadow:8px 8px 0 var(--teal);display:flex;flex-direction:column;align-items:center;justify-content:center;color:var(--white);font-size:14px}
.video svg{margin-bottom:10px}
.divider{height:1px;background:var(--rule);margin:0 60px}

/* features */
.features{height:732px;display:flex;padding:40px 80px 0 150px}
.person{width:250px;height:660px;background:linear-gradient(180deg,#e9e6e2 0%,#cfd3d8 25%,#3a3f4a 40%,#2b2f38 100%);border-radius:6px}
.feature-grid{display:grid;grid-template-columns:300px 300px;column-gap:50px;row-gap:44px;margin:50px 0 0 60px;align-content:start}
.feature-head{display:flex;align-items:center;gap:14px;margin-bottom:16px}
.icon{width:56px;height:56px;border-radius:50%;background:var(--teal);display:flex;align-items:center;justify-content:center;flex:none}
.feature h3{font-size:11px;font-weight:600;color:var(--ink);letter-spacing:.5px}
.feature p{font-size:12px;color:var(--muted)}

/* cta band */
.cta-band{height:180px;background:var(--teal);display:flex;align-items:center;justify-content:space-between;padding:0 80px;color:var(--white)}
.cta-band h3{font-size:15px;font-weight:700;letter-spacing:1px;white-space:nowrap}
.inline-form{display:flex;border:1px solid rgba(255,255,255,.8);width:520px;height:50px;flex:none}
.inline-form .field{flex:1}
.inline-form .go{width:170px;border-left:1px solid rgba(255,255,255,.8);display:flex;align-items:center;justify-content:center;font-family:"Montserrat",Arial,sans-serif;font-size:12px;font-weight:600;letter-spacing:1px;white-space:nowrap}

/* split */
.split{height:460px;display:flex;position:relative;overflow:hidden}
.split-text{position:relative;z-index:1;width:620px;padding:50px 0 0 90px}
.split-text h2{font-size:28px;line-height:1.25;font-weight:700;color:var(--ink);white-space:nowrap}
.split-text .sub{font-family:"Montserrat",Arial,sans-serif;color:var(--ink);font-weight:600;font-size:15px;margin:8px 0}
.split-text .accent-rule{margin:18px 0 22px}
.split-text p{font-size:13px;margin-bottom:14px;width:460px}
.split-text .btn{margin-top:4px}
.office-photo{position:absolute;right:0;top:0;width:580px;height:460px;background:linear-gradient(90deg,#ffffff 0%,#e4eaf0 25%,#c9d3dc 60%,#aab8c4 100%)}

/* newsletter */
.newsletter{height:340px;background:var(--dark);display:flex;align-items:center;padding:0 90px;color:var(--white)}
.news-mark{width:170px;height:170px;background:var(--darker);flex:none}
.news-copy{margin-left:40px;width:380px;flex:none}
.news-copy h2{font-size:28px;font-weight:700;letter-spacing:1px;white-space:nowrap}
.news-copy p{font-size:15px}
.news-form{display:flex;height:46px;flex:none}
.news-form .field{width:280px;background:var(--white);color:var(--muted);font-size:12px;padding:12px 16px}
.news-form .btn{padding:0 28px;line-height:46px}

/* footer */
.footer{height:440px;display:flex;padding:70px 90px 0;gap:70px}
.footer-about{width:340px}
.footer-about .brand{color:var(--ink);margin-bottom:22px}
.footer-about .brand-square{background:var(--ink)}
.footer-about p{font-size:12px;margin-bottom:24px}
.socials{display:flex;gap:12px}
.socials span{width:30px;height:30px;border-radius:50%;background:var(--ink)}
.footer-col{width:180px}
.footer-col h4{font-size:15px;font-weight:700;color:var(--ink);letter-spacing:1px;margin-bottom:20px}
.footer-col li{list-style:none;font-size:11px;letter-spacing:.5px;text-transform:uppercase;padding:6px 0 6px 14px;border-bottom:1px solid var(--rule);position:relative}
.footer-col li::before{content:"›";position:absolute;left:0;color:var(--teal)}
.office li{text-transform:none;display:flex;gap:10px;align-items:center;padding-left:0;border:0}
.office li::before{content:none}
.dot{width:14px;height:14px;border-radius:50%;background:var(--teal);flex:none}
.copyright{height:96px;background:var(--darker);color:var(--muted);font-size:12px;display:flex;align-items:center;justify-content:center}
</style>
</head>
<body>

<header class="hero">
  <div class="hero-bg" role="img" aria-label="City skyline photo behind a person looking out at dusk"></div>
  <div class="topbar">
    <div class="brand"><span class="brand-square"></span>Talvoxa</div>
    <nav class="nav">
      <span>PRODUCTS</span><span>PRICING</span><span>RESOURCES</span><span>BLOG</span><span>LOG IN</span>
      <svg width="16" height="16" viewBox="0 0 16 16"><circle cx="6.5" cy="6.5" r="5" fill="none" stroke="#fff" stroke-width="2"/><line x1="10.5" y1="10.5" x2="15" y2="15" stroke="#fff" stroke-width="2"/></svg>
    </nav>
  </div>
  <div class="hero-copy">
    <h1>PELLENTESQUE GRAVIDA<br>RISUS ELEIFEND ERAT</h1>
    <p>Mauris congue et orci at placerat. Sed elementum pellentesque facilisis. Duis ac velit ex.</p>
    <span class="btn">GET STARTED</span>
  </div>
</header>

<section class="about">
  <div class="about-text">
    <h2 class="section-title">ABOUT US</h2>
    <div class="kicker">WELCOME TO TALVOXA</div>
    <div class="accent-rule"></div>
    <p>Lorem ipsum dolor sit amet, consectetuer adipiscing elit, sed diam nonummy nibh euismod tincidunt ut laoreet dolore magna aliquam erat volutpat. Ut wisi enim ad minim veniam, quis nostrud exerci tation ullamcorper suscipit lobortis nisl ut aliquip ex ea commodo consequat.</p>
    <p>Duis autem vel eum iriure dolor in hendrerit in vulputate velit esse molestie consequat, vel illum dolore eu feugiat nulla facilisis at vero eros et accumsan et iusto odio dignissim qui blandit praesent luptatum zzril delenit augue duis dolore te feugait nulla facilisi. Nam liber tempor cum soluta nobis eleifend option congue.</p>
  </div>
  <div class="video" role="img" aria-label="Video preview of the platform in use">
    <svg width="46" height="46" viewBox="0 0 46 46"><circle cx="23" cy="23" r="21" fill="none" stroke="#fff" stroke-width="2"/><polygon points="18,14 33,23 18,32" fill="#fff"/></svg>
    Play video
  </div>
</section>

<div class="divider"></div>

<section class="features">
  <div class="person" role="img" aria-label="Photo of a businessman in a dark suit standing"></div>
  <div class="feature-grid">
    <div class="feature">
      <div class="feature-head"><span class="icon"><svg width="24" height="24" viewBox="0 0 24 24"><rect x="3" y="5" width="18" height="12" rx="2" fill="#fff"/><polygon points="7,17 7,21 11,17" fill="#fff"/></svg></span><h3>CONSECTETUR LOBORTIS</h3></div>
      <p>Lorem ipsum dolor sit amet, consectetuer adipiscing elit, sed diam nonummy nibh euismod tincidunt ut laoreet dolore magna aliquam erat.</p>
    </div>
    <div class="feature">
      <div class="feature-head"><span class="icon"><svg width="24" height="24" viewBox="0 0 24 24"><circle cx="12" cy="12" r="8" fill="none" stroke="#fff" stroke-width="2.5"/><circle cx="12" cy="12" r="3" fill="#fff"/></svg></span><h3>MAURIS CONGUE ET ORCI</h3></div>
      <p>Lorem ipsum dolor sit amet, consectetuer adipiscing elit, sed diam nonummy nibh euismod tincidunt ut laoreet dolore magna aliquam erat.</p>
    </div>
    <div class="feature">
      <div class="feature-head"><span class="icon"><svg width="24" height="24" viewBox="0 0 24 24"><rect x="4" y="4" width="16" height="16" rx="2" fill="none" stroke="#fff" stroke-width="2.5"/><polyline points="8,12 11,15 16,9" fill="none" stroke="#fff" stroke-width="2.5"/></svg></span><h3>DONEC IMPERDIET TALVOXA</h3></div>
      <p>Lorem ipsum dolor sit amet, consectetuer adipiscing elit, sed diam nonummy nibh euismod tincidunt ut laoreet dolore magna aliquam erat.</p>
    </div>
    <div class="feature">
      <div class="feature-head"><span class="icon"><svg width="24" height="24" viewBox="0 0 24 24"><circle cx="8" cy="9" r="3" fill="#fff"/><circle cx="16" cy="9" r="3" fill="#fff"/><rect x="3" y="14" width="18" height="5" rx="2" fill="#fff"/></svg></span><h3>PELLENTESQUE ID EFFICITUR</h3></div>
      <p>Lorem ipsum dolor sit amet, consectetuer adipiscing elit, sed diam nonummy nibh euismod tincidunt ut laoreet dolore magna aliquam erat.</p>
    </div>
    <div class="feature">
      <div class="feature-head"><span class="icon"><svg width="24" height="24" viewBox="0 0 24 24"><path d="M12 3 L21 12 L12 21 L3 12 Z" fill="#fff"/></svg></span><h3>PELLENTESQUE GRAVIDA RISUS</h3></div>
      <p>Lorem ipsum dolor sit amet, consectetuer adipiscing elit, sed diam nonummy nibh euismod tincidunt ut laoreet dolore magna aliquam erat.</p>
    </div>
    <div class="feature">
      <div class="feature-head"><span class="icon"><svg width="24" height="24" viewBox="0 0 24 24"><circle cx="12" cy="8" r="4" fill="#fff"/><path d="M4 21 C4 14 20 14 20 21 Z" fill="#fff"/></svg></span><h3>FERMENTUM EUCESTIQUE</h3></div>
      <p>Lorem ipsum dolor sit amet, consectetuer adipiscing elit, sed diam nonummy nibh euismod tincidunt ut laoreet dolore magna aliquam erat.</p>
    </div>
  </div>
</section>

<section class="cta-band">
  <h3>DONEC IMPERDIET PHARETRA ARCU EGET LACINIA</h3>
  <div class="inline-form"><span class="field"></span><span class="go">GET STARTED</span></div>
</section>

<section class="split">
  <div class="split-text">
    <h2>CURABITUR CURSUS<br>CONSECTETUR MAGNA EGET</h2>
    <div class="sub">Lorem ipsum dolor sit amet</div>
    <div class="accent-rule"></div>
    <p>Lorem ipsum dolor sit amet, consectetuer adipiscing elit, sed diam nonummy nibh euismod tincidunt ut laoreet dolore magna aliquam erat volutpat. Ut wisi enim ad minim veniam.</p>
    <p>Sed ullamcorper mattis lorem tincidunt tempor lobortis nisl ut aliquip ex ea commodo consequat. Duis autem vel eum iriure dolor in hendrerit in vulputate velit.</p>
    <span class="btn">GET STARTED</span>
  </div>
  <div class="office-photo" role="img" aria-label="Photo of a man working at a laptop in a bright office"></div>
</section>

<section class="newsletter">
  <div class="news-mark"></div>
  <div class="news-copy">
    <h2>NEWSLETTER SIGN-UP</h2>
    <p>We make sure you do not miss any news</p>
  </div>
  <div class="news-form"><span class="field">Enter your e-mail</span><span class="btn">SIGN UP</span></div>
</section>

<footer class="footer">
  <div class="footer-about">
    <div class="brand"><span class="brand-square"></span>Talvoxa</div>
    <p>Lorem ipsum dolor sit amet, consectetuer adipiscing elit, sed diam nonummy nibh euismod tincidunt ut laoreet dolore magna aliquam erat volutpat. Ut wisi enim ad minim veniam, quis nostrud exerci tation ullamcorper suscipit lobortis nisl ut aliquip ex ea commodo consequat.</p>
    <div class="socials"><span></span><span></span><span></span><span></span></div>
  </div>
  <div class="footer-col">
    <h4>INFORMATION</h4>
    <ul><li>Home</li><li>Blog</li><li>Contact</li><li>About us</li><li>Projects</li></ul>
  </div>
  <div class="footer-col">
    <h4>RESOURCES</h4>
    <ul><li>Get a demo</li><li>Documentation</li><li>Developers</li><li>Pricing</li><li>Security</li></ul>
  </div>
  <div class="footer-col office" style="width:230px">
    <h4>OUR OFFICE</h4>
    <ul>
      <li><span class="dot"></span>18 Corvel Lane, Harbor District</li>
      <li><span class="dot"></span>Northbay 20410</li>
      <li><span class="dot"></span>+00 555 0148</li>
      <li><span class="dot"></span>hello@talvoxa-demo.com</li>
      <li><span class="dot"></span>Mon - Sat: 9:00 - 18:00</li>
    </ul>
  </div>
</footer>

<div class="copyright">© 2016 Talvoxa. All rights reserved.</div>

</body>
</html>
```